New business! Essential Oils Label for 10 mL Essential Oils Bottles

I need a label design for my new essential oils business. The design should be easily transferable between products. Content should include:
label size W x H 1.25 x 2.875

LAVENDER
Lavandula angustifolia
VOLMIRAâ„¢
100% PURE ESSENTIAL OIL
Net 10 mL
For promotions and additional product information visit fb.com/VolmiraOils
VolmiraOils.com
Marlow Point, ST 33871
888-555-KIPO (5476)
Indications: Massage (10 drops of carrier oil for every drop of essential oil), Bath (10 drops of essential oil) or Inhalation (2-4 drops essential of on a tissue).
EXTERNAL USE ONLY- DILUTE BEFORE APPLICATION
Caution: Do not ingest the oil. Sensitive skin may be irritated by topical use. Avoid contact with eyes. Consult your healthcare practitioner before use. Store oil away from children and pets. Not meant for use during pregnancy. Seek medical care immediately if adverse reaction is experienced.

Target Market(s)

ONLINE SHOPPERS

Industry/Entity Type

Business

Font styles to use
Serif
Sans Serif

Colors

Designer to choose colors to be used in the design.

Requirements
Must have
• CONTENT AS LISTED IN PROJECT DESCRIPTION, LOGO (ATTACHED)
Nice to have
• Files with easily transferable content so the same label design can be used for multiple products.
Should not have
• Too small of print, difficult to read

```html
<!DOCTYPE html>
<html lang="en">
<head>
<meta charset="utf-8">
<title>Volmira Lavender Essential Oil – Label &amp; Carton</title>
<link rel="stylesheet" href="https://fonts.googleapis.com/css2?family=Montserrat:wght@300;400;500&family=Lora:wght@400&display=swap">
<style>
  :root {
    --bg: #ececec;
    --ink: #141414;
    --panel-black: #151515;
    --plum: #7c3b6a;
    --plum-text: #c27bb0;
    --silver-light: #e6e6e6;
    --silver-dark: #8a8a8a;
    --white: #ffffff;
    --muted: #cfcfcf;
    --pale-plum: #e7cce0;
  }
  * { margin: 0; padding: 0; box-sizing: border-box; }
  html, body { width: 1200px; height: 900px; overflow: hidden; background: var(--bg); }
  body { font-family: "Montserrat", sans-serif; color: var(--ink); position: relative; }

  .brand-mark {
    position: absolute; top: 92px; left: 0; width: 1200px;
    text-align: center; font-weight: 400; font-size: 72px; letter-spacing: 4px;
    color: var(--ink); line-height: 1;
  }
  .brand-mark sup, .tm { font-size: 0.3em; vertical-align: top; letter-spacing: 0; margin-left: 2px; }

  .artwork { position: absolute; top: 290px; left: 170px; display: flex; gap: 60px; align-items: flex-start; }

  .carton { display: flex; }
  .carton-panel { width: 200px; height: 420px; display: flex; flex-direction: column; }
  .carton-panel .upper { background: var(--panel-black); flex: 0 0 270px; color: var(--white); padding: 20px 16px; position: relative; }
  .silver-rule { height: 10px; flex: 0 0 10px; background: linear-gradient(90deg, var(--silver-dark), var(--silver-light) 50%, var(--silver-dark)); }
  .carton-panel .lower { background: var(--plum); flex: 1; color: var(--white); padding: 16px; position: relative; }
  .carton-side { border-right: 1px solid #2c2c2c; }

  .fine-print { font-size: 6.5px; line-height: 1.35; color: var(--muted); }
  .fine-print p { margin-bottom: 6px; }
  .fine-print strong { color: var(--white); font-weight: 500; }
  .lower.fine-print { color: #f0dbe9; }

  .front-brand { text-align: center; font-size: 20px; letter-spacing: 1.5px; margin-top: 40px; }
  .front-name { position: absolute; bottom: 34px; left: 16px; font-size: 22px; letter-spacing: 4px; font-weight: 400; }
  .front-latin { position: absolute; bottom: 18px; left: 30px; font-size: 9px; color: var(--muted); }
  .front-pure { font-size: 17px; font-weight: 300; color: var(--pale-plum); margin-top: 6px; }
  .front-essential { font-family: "Lora", serif; font-size: 11px; letter-spacing: 3px; color: var(--pale-plum); margin-top: 4px; }
  .front-volume { position: absolute; bottom: 18px; left: 16px; font-size: 11px; font-weight: 300; color: var(--pale-plum); }

  .bottle-label { width: 460px; height: 200px; display: flex; flex-direction: column; margin-top: 110px; }
  .bottle-label .band-top { background: var(--panel-black); height: 56px; color: var(--white); display: flex; align-items: center; justify-content: center; font-size: 24px; letter-spacing: 1.5px; }
  .bottle-label .band-mid { background: var(--plum); height: 78px; color: var(--white); text-align: center; padding-top: 8px; }
  .label-name { font-size: 28px; letter-spacing: 5px; line-height: 1.1; }
  .label-latin { font-size: 11px; color: #ead3e4; margin-top: 2px; }
  .bottle-label .band-bottom { background: var(--panel-black); flex: 1; text-align: center; position: relative; }
  .pure-pill {
    position: absolute; top: -14px; left: 50%; transform: translateX(-50%);
    background: linear-gradient(180deg, var(--silver-light), #b9b9b9);
    border-radius: 14px; padding: 3px 16px; font-size: 16px; font-weight: 300; color: var(--ink); white-space: nowrap;
  }
  .label-essential { font-family: "Lora", serif; font-size: 15px; letter-spacing: 3.5px; color: var(--plum-text); padding-top: 22px; }
</style>
</head>
<body>

  <h1 class="brand-mark">VOLMIRA<sup>TM</sup></h1>

  <main class="artwork">
    <section class="carton" aria-label="Carton panels">
      <div class="carton-panel carton-side">
        <div class="upper fine-print">
          <p><strong>Indications:</strong> Massage (10 drops of carrier oil for every drop of essential oil), Bath (10 drops of essential oil) or Inhalation (2-4 drops essential oil on a tissue).</p>
          <p><strong>EXTERNAL USE ONLY – DILUTE BEFORE APPLICATION</strong></p>
          <p><strong>Caution:</strong> Do not ingest the oil. Sensitive skin may be irritated by topical use. Avoid contact with eyes. Consult your healthcare practitioner before use. Store oil away from children and pets. Not meant for use during pregnancy. Seek medical care immediately if adverse reaction is experienced.</p>
        </div>
        <div class="silver-rule"></div>
        <div class="lower fine-print">
          <p>For promotions and additional product information visit fb.com/VolmiraOils</p>
          <p>VolmiraOils.com<br>Marlow Point, ST 33871<br>888-555-KIPO (5476)</p>
        </div>
      </div>

      <div class="carton-panel carton-front">
        <div class="upper">
          <div class="front-brand">VOLMIRA<span class="tm">TM</span></div>
          <div class="front-name">LAVENDER</div>
          <div class="front-latin">Lavandula angustifolia</div>
        </div>
        <div class="silver-rule"></div>
        <div class="lower">
          <div class="front-pure">100% PURE</div>
          <div class="front-essential">ESSENTIAL OIL</div>
          <div class="front-volume">0.33 fl. oz (10 mL)</div>
        </div>
      </div>
    </section>

    <section class="bottle-label" aria-label="Bottle label">
      <div class="band-top">VOLMIRA<span class="tm">TM</span></div>
      <div class="silver-rule"></div>
      <div class="band-mid">
        <div class="label-name">LAVENDER</div>
        <div class="label-latin">Lavandula angustifolia</div>
      </div>
      <div class="band-bottom">
        <div class="pure-pill">100% PURE</div>
        <div class="label-essential">ESSENTIAL OIL</div>
      </div>
    </section>
  </main>

</body>
</html>
```